Expedited Project Word Template, envelopes and powerpoint template
no business card needed already have
n/a
2486 Quill Basin Lane
Orlen Falls, OH 44921
info@tivelmora.com
-uploaded logo needs to have ® symbol placed after the word "growing"
-already have business cards just need word template and letterhead and envelopes
-business focused on renewable energies/fresh produce production/environment, looking for classic corporate look
--trying to limit cost of printing as a start-up, so preference is for white background and then use color to highlight key areas
--powerpoint template looking for title slide, section break slide, main content slide, table slide, and image slide. template should include page numbering and private/confidential in the footer.
Here is how my biz card looks -- please note the tag line on this copy is correct"
"where technology and nature meet"

```html
<!DOCTYPE html>
<html lang="en">
<head>
<meta charset="utf-8">
<title>Tivelmora Farms – Stationery and Presentation Templates</title>
<link rel="stylesheet" href="https://fonts.googleapis.com/css2?family=Arimo:wght@400;700&display=swap">
<style>
  :root{
    --board:#cfcfcf;
    --paper:#ffffff;
    --brand-green:#8cc63f;
    --brand-green-soft:#b9dc8a;
    --rule-green:#a6d15a;
    --title-cyan:#2ec4c9;
    --sky:#7fe3f0;
    --field:#8cb43c;
    --soil:#6f7f3a;
    --ink:#333333;
    --ink-soft:#777777;
    --window:#e6e6e6;
    --shadow:0 3px 8px rgba(0,0,0,.35);
  }
  *{box-sizing:border-box;margin:0;padding:0}
  html,body{width:1200px;height:988px;overflow:hidden}
  body{background:var(--board);font-family:"Arimo",Arial,sans-serif;color:var(--ink);position:relative}

  .piece{position:absolute;background:var(--paper);box-shadow:var(--shadow);overflow:hidden}

  /* brand lockup */
  .brand{display:flex;flex-direction:column;align-items:center;text-align:center}
  .brand-dot{width:16px;height:16px;border-radius:50%;background:var(--brand-green);margin-bottom:6px}
  .brand-name{color:var(--brand-green);font-weight:700;letter-spacing:.5px;white-space:nowrap}
  .brand-tagline{color:var(--ink-soft);font-size:7px;margin-top:3px;white-space:nowrap}

  /* letterhead */
  .letterhead{left:22px;top:67px;width:622px;height:870px}
  .letterhead .brand{position:absolute;left:0;right:0;top:40px}
  .letterhead .brand-name{font-size:13px}
  .letterhead .header-rule{position:absolute;left:16px;right:16px;top:100px;height:2px;background:var(--rule-green)}
  .letterhead .reference{position:absolute;left:420px;top:108px;font-size:9px;line-height:14px}
  .letterhead .reference span{display:inline-block;width:70px;border-bottom:1px solid #bbb;margin-left:6px}
  .letterhead .footer-rule{position:absolute;left:16px;right:16px;top:832px;height:1px;background:#999}
  .letterhead .footer{position:absolute;left:0;right:0;top:838px;text-align:center;font-size:8px;line-height:10px;color:var(--ink)}
  .letterhead .footer .ico{display:inline-block;width:7px;height:6px;background:var(--ink);border-radius:1px;margin-right:4px;vertical-align:middle}

  /* envelope */
  .envelope{left:649px;top:21px;width:543px;height:228px}
  .envelope .brand{position:absolute;left:70px;width:170px;top:12px}
  .envelope .brand-dot{width:10px;height:10px;margin-bottom:3px}
  .envelope .brand-name{font-size:7px}
  .envelope .return{font-size:5.5px;line-height:7px;color:var(--ink);margin-top:3px}
  .envelope .window{position:absolute;left:19px;top:94px;width:259px;height:96px;background:var(--window);border:1px solid #b5b5b5;border-radius:6px}

  /* slides */
  .slide-title{left:690px;top:262px;width:502px;height:375px}
  .slide-title .backdrop{position:absolute;inset:0;background:linear-gradient(180deg,var(--sky) 0%,#e9fbfc 30%,#ffffff 42%,#d7eab0 58%,var(--field) 82%,var(--soil) 100%)}
  .slide-title .brand{position:absolute;left:12px;width:180px;top:50px}
  .slide-title .brand-name{font-size:9px}
  .slide-title .rule-h{position:absolute;left:12px;right:0;top:138px;height:1px;background:rgba(255,255,255,.9)}
  .slide-title .rule-v{position:absolute;left:220px;top:0;width:1px;height:255px;background:rgba(255,255,255,.9)}
  .slide-title .title{position:absolute;left:235px;right:10px;top:172px;text-align:center;color:var(--title-cyan);font-weight:700;font-size:27px;line-height:34px}

  .slide-section{left:736px;top:642px;width:456px;height:335px}
  .slide-section .backdrop{position:absolute;inset:0;background:linear-gradient(180deg,var(--sky) 0%,#e7fafb 22%,#ffffff 45%,#eef6dc 75%,#cfe4a6 100%)}
  .slide-section .corner-dot{position:absolute;left:26px;top:18px;width:14px;height:14px;border-radius:50%;background:var(--brand-green)}
  .slide-section .subtitle{position:absolute;left:200px;top:16px;font-weight:700;font-size:15px;color:var(--ink)}
  .slide-section .rule{position:absolute;left:60px;right:0;top:46px;height:1px;background:#9fcfd6}
  .slide-section .brand{position:absolute;left:0;right:0;top:128px}
  .slide-section .brand-dot{background:var(--brand-green-soft)}
  .slide-section .brand-name{font-size:15px;color:var(--brand-green-soft);font-weight:400}
</style>
</head>
<body>

<section class="piece letterhead" aria-label="Letterhead">
  <div class="brand">
    <div class="brand-dot"></div>
    <div class="brand-name">TIVELMORA FARMS®</div>
    <div class="brand-tagline">where technology and nature meet</div>
  </div>
  <div class="header-rule"></div>
  <div class="reference">Reference no<span></span><br>Date<span style="width:102px"></span></div>
  <div class="footer-rule"></div>
  <div class="footer">
    2486 Quill Basin Lane, Orlen Falls, OH 44921<br>
    <span class="ico"></span>555-014-2290<br>
    <span class="ico"></span>info@tivelmora.com
  </div>
</section>

<section class="piece envelope" aria-label="Envelope">
  <div class="brand">
    <div class="brand-dot"></div>
    <div class="brand-name">TIVELMORA FARMS®</div>
    <div class="return">2486 Quill Basin Lane<br>Orlen Falls, OH 44921</div>
  </div>
  <div class="window"></div>
</section>

<section class="piece slide-title" aria-label="Title slide">
  <div class="backdrop" role="img" aria-label="Sky to green field gradient with a perspective grid"></div>
  <div class="brand">
    <div class="brand-dot"></div>
    <div class="brand-name">TIVELMORA FARMS®</div>
    <div class="brand-tagline">where technology and nature meet</div>
  </div>
  <div class="rule-h"></div>
  <div class="rule-v"></div>
  <h1 class="title">PRESENTATION<br>TITLE</h1>
</section>

<section class="piece slide-section" aria-label="Section slide">
  <div class="backdrop"></div>
  <div class="corner-dot"></div>
  <h2 class="subtitle">Presentation Subtitle</h2>
  <div class="rule"></div>
  <div class="brand">
    <div class="brand-dot"></div>
    <div class="brand-name">TIVELMORA FARMS®</div>
  </div>
</section>

</body>
</html>
```